Web Site for Strategy and Technology Consulting Company

We are looking for a website design that engages potential customers to understand our services and contact us. In this contest, we are looking for a homepage design, but the winning designer will be favored for the design of some of the more complicated interior pages of the site. An additional contest (or contests) for these pages will be added soon.

PLATROM AND RESPONSIVE DESIGN
The site will be implemented in WordPress using the Elementor page builder.
We are looking for a design that will look good on phones are well as laptop browsers.

UPLOADED FILES INCLUDE:
1a A wireframe of the homepage we are looking for. The Uploaded PDF also includes a draft of the text proposed for the homepage. Designers are free to go beyond the wireframe, but all elements of the wireframe should be included.
1b A Word document with the draft text of the homepage.
2a-d The Corvanta logo. Two versions are included – a dark version which works well against a light background, and a light version which works well against a dark background.
3 The Corvanta color palette with HEX and RGB values. Designers are not limited to this palette, but colors should be complementary.
4 A draft of the homepage menu
5 Service sheets with information on the services we provide

MORE ABOUT CORVANTA
Corvanta is a consulting company focused on transforming businesses through software. Our tagline, “Transformation Delivered,” recognizes the gap business often have between business transformation and the software they end up with. By listening to our customers and understanding their vision and where they are, we help get our customers where they want to go.

We increase our capability by working with many consultants and partners, allowing us to provide our customers with the best people and the software that best suits them.

Industry/Entity Type

Consulting

Number of Pages Required

1 page

Font styles to use
Sans Serif

Requirements
Must have
• the content represented on the wireframe uploaded
Nice to have
• interactive features, such as roll-over icons that reveal additional information

```html
<!DOCTYPE html>
<html lang="en">
<head>
<meta charset="utf-8">
<title>Corvanta — Transformation Delivered</title>
<link href="https://fonts.googleapis.com/css2?family=Montserrat:wght@600;700;800&family=Lato:wght@400;700&display=swap" rel="stylesheet">
<style>
:root{
  --navy:#0a2134;
  --navy-deep:#071828;
  --teal:#0f3347;
  --blue:#1f5a93;
  --blue-card:#1d4f7e;
  --grey-card:#6c7b80;
  --yellow:#f5c518;
  --white:#ffffff;
  --muted:#c9d6e0;
  --testi:#56646d;
}
*{margin:0;padding:0;box-sizing:border-box}
html,body{width:1200px;height:4047px;overflow:hidden}
body{position:relative;background:var(--navy);font-family:'Lato',sans-serif;color:var(--white)}
.abs{position:absolute}
h1,h2,h3{font-family:'Montserrat',sans-serif;font-weight:800;letter-spacing:.5px}
.btn{position:absolute;display:flex;align-items:center;justify-content:center;font-family:'Montserrat',sans-serif;font-weight:700;font-size:13px;letter-spacing:.3px;background:var(--blue);color:var(--white);text-transform:uppercase}
.btn.light{background:var(--white);color:var(--navy)}

/* top bar */
.topbar{top:0;left:0;width:1200px;height:41px;background:linear-gradient(90deg,#1b4f80,#2466a4)}
.topbar .social{position:absolute;top:13px;width:14px;height:14px;border-radius:50%;background:var(--white);opacity:.9}
.phone-tab{top:0;left:943px;width:190px;height:41px;background:var(--navy);border-radius:0 0 8px 8px;color:var(--yellow);font-size:14px;display:flex;align-items:center;justify-content:center;gap:6px}

/* hero */
.hero{top:41px;left:0;width:1200px;height:740px;background:linear-gradient(110deg,#1c2a36 0%,#2a3b48 35%,#1a2733 70%,#0f1c27 100%)}
.brand{font-family:'Lato',sans-serif;font-weight:400;color:var(--white);font-size:50px;letter-spacing:.5px}
.nav a{position:absolute;top:71px;font-family:'Montserrat',sans-serif;font-weight:600;font-size:13px;color:var(--white);text-decoration:none}
.hero-title{top:315px;left:665px;font-size:51px;line-height:62px;color:var(--white)}
.hero-sub{top:455px;left:665px;font-size:17px;font-weight:700}
.hero-sub span{color:var(--yellow)}

/* services */
.section-2{top:740px;left:0;width:1200px;height:860px;background:linear-gradient(120deg,#0c2438 0%,#113548 60%,#0e2b3e 100%)}
.eyebrow{font-family:'Lato',sans-serif;font-size:18px;font-weight:400;letter-spacing:.5px;text-transform:uppercase}
.sec-title{font-size:44px;line-height:56px}
.lead{font-size:17px;line-height:26px;color:#e6eef4}
.card{position:absolute;width:261px;height:267px;border-radius:4px;padding:0 22px}
.card.blue{background:var(--blue-card)}
.card.grey{background:var(--grey-card)}
.card .icon{width:56px;height:56px;border-radius:50%;margin-top:56px}
.card h3{font-family:'Lato',sans-serif;font-weight:400;font-size:20px;line-height:26px;margin-top:18px}
.card.grey h3{color:var(--yellow)}
.card p{font-size:14px;line-height:19px;margin-top:12px;color:#dbe5ec}

/* people */
.photo{position:absolute}
.bullets li{list-style:none;position:relative;padding-left:18px;font-weight:700;font-size:14px;line-height:20px;margin-bottom:18px}
.bullets li::before{content:"";position:absolute;left:0;top:6px;width:8px;height:8px;background:var(--yellow)}

/* testimonials */
.testimonials{top:2259px;left:0;width:1200px;height:700px;background:linear-gradient(180deg,#5b6a73,#4e5d66)}
.arrow{position:absolute;top:2697px;width:96px;height:50px;border-radius:25px;background:rgba(255,255,255,.14)}

/* technology */
.tech-card{position:absolute;top:3074px;width:341px;height:390px}
.tech-card span{position:absolute;left:18px;bottom:26px;font-family:'Lato',sans-serif;font-size:20px;font-weight:700}

/* footer */
.footer{top:3542px;left:0;width:1200px;height:505px;background:var(--navy-deep)}
.f-head{position:absolute;top:3622px;font-family:'Lato',sans-serif;font-size:21px;font-weight:700;color:var(--yellow)}
.f-list{position:absolute;top:3676px;list-style:none;font-size:13px;line-height:30.6px}
.vline{position:absolute;top:3618px;width:1px;height:240px;background:rgba(255,255,255,.12)}
</style>
</head>
<body>

<!-- top bar -->
<div class="abs topbar">
  <span class="social" style="left:63px"></span>
  <span class="social" style="left:96px"></span>
  <span class="social" style="left:135px"></span>
</div>
<div class="abs phone-tab">
  <svg width="12" height="12" viewBox="0 0 24 24"><path fill="#f5c518" d="M6.6 10.8a15.1 15.1 0 0 0 6.6 6.6l2.2-2.2a1 1 0 0 1 1-.25 11.4 11.4 0 0 0 3.6.57 1 1 0 0 1 1 1V20a1 1 0 0 1-1 1A17 17 0 0 1 3 4a1 1 0 0 1 1-1h3.5a1 1 0 0 1 1 1c0 1.25.2 2.45.57 3.6a1 1 0 0 1-.25 1z"/></svg>
  +2 (555) 240 7310
</div>

<!-- hero -->
<div class="abs hero" role="img" aria-label="Team of consultants working together in a modern office, with a large letter A built from blue and yellow squares"></div>
<div class="abs brand" style="top:52px;left:66px">Corvanta</div>
<nav class="nav">
  <a style="left:617px">ABOUT</a>
  <a style="left:712px">SERVICE</a>
  <a style="left:815px">INSIGHTS</a>
  <a style="left:925px">JOIN US</a>
</nav>
<div class="btn" style="top:61px;left:1005px;width:128px;height:37px">Contact Us</div>
<h1 class="abs hero-title">TRANSFORMATION<br>DELIVERED</h1>
<p class="abs hero-sub">We do more for our customers <span>than implement software.</span></p>
<div class="btn" style="top:500px;left:665px;width:124px;height:43px">Our Story</div>

<!-- services -->
<div class="abs section-2"></div>
<svg class="abs" style="top:660px;left:0" width="1200" height="130" viewBox="0 0 1200 130">
  <path d="M0 78 C160 40 330 22 500 30 C680 40 860 80 1000 80 C1090 80 1160 62 1200 48 L1200 130 L0 130Z" fill="#0c2438"/>
  <path d="M0 104 C150 50 330 20 520 28 C340 30 170 62 0 78Z" fill="#f5c518"/>
</svg>

<div class="abs eyebrow" style="top:927px;left:65px">Transformation</div>
<h2 class="abs sec-title" style="top:957px;left:65px">SUPPORTED<br>BY TECHNOLOGY</h2>
<p class="abs lead" style="top:1098px;left:68px;width:460px">During our early years, Corvanta focused only on business transformation. We came to realize that successful transformation often depended on quality software implementations, and often more than one. Now we focus on five things, the five things most businesses need to reach their goals.</p>
<div class="btn light" style="top:1291px;left:69px;width:135px;height:46px">View All</div>

<div class="card blue" style="top:828px;left:578px">
  <div class="icon" style="background:radial-gradient(circle,#5fc4e8,#2a6fb5)"></div>
  <h3>Business<br>Transformation</h3>
  <p>Define and execute your strategy.</p>
</div>
<div class="card grey" style="top:872px;left:872px">
  <div class="icon" style="background:#ffffff;opacity:.85"></div>
  <h3>ERP<br>Implementations</h3>
  <p>Assess, upgrade, and implement ERP solutions to meet your needs.</p>
</div>
<div class="card blue" style="top:1131px;left:578px">
  <div class="icon" style="background:linear-gradient(135deg,#e85a6a,#f5c518)"></div>
  <h3>CRM<br>Implementations</h3>
  <p>Take your relationships to the next level.</p>
</div>
<div class="card blue" style="top:1175px;left:872px">
  <div class="icon" style="background:linear-gradient(135deg,#7ec8f0,#f5c518)"></div>
  <h3>BI<br>and Data</h3>
  <p>Discover, connect, and trust your data.</p>
</div>

<svg class="abs" style="top:1490px;left:0" width="1200" height="110" viewBox="0 0 1200 110">
  <path d="M0 0 C120 40 260 84 480 86 C700 88 900 60 1200 30 L1200 110 L0 110Z" fill="#0a2134"/>
  <path d="M0 0 C120 40 260 84 480 86 C300 100 120 80 0 50Z" fill="#f5c518"/>
</svg>

<!-- people -->
<div class="photo" style="top:1660px;left:71px;width:94px;height:94px;background:linear-gradient(135deg,#ffffff,#dfe9ee)" role="img" aria-label="Bright window light"></div>
<div class="photo" style="top:1754px;left:165px;width:201px;height:201px;background:linear-gradient(135deg,#c9b3a2,#7a3a3f 60%,#3e2a2e)" role="img" aria-label="Two colleagues looking at a laptop together"></div>
<div class="photo" style="top:1811px;left:380px;width:156px;height:156px;background:linear-gradient(135deg,#9db69a,#3160b8 70%)" role="img" aria-label="Professional woman in blue using a tablet"></div>
<div class="photo" style="top:1968px;left:194px;width:68px;height:68px;background:linear-gradient(135deg,#a8b0a4,#6e7a77)" role="img" aria-label="Office detail"></div>
<div class="photo" style="top:1980px;left:284px;width:202px;height:202px;background:linear-gradient(135deg,#c04a55,#2f5fb8 55%,#1b1f24)" role="img" aria-label="Colleagues reviewing a tablet"></div>

<div class="abs eyebrow" style="top:1655px;left:613px">Resources</div>
<h2 class="abs sec-title" style="top:1686px;left:613px">IT’S THE PEOPLE</h2>
<p class="abs lead" style="top:1765px;left:613px;width:520px">The world has changed in the past twenty years. The people you need might not all work for one company. Our clients want the best resources, available quickly. That’s why, in addition to our team of experts, we partner with:</p>
<ul class="abs bullets" style="top:1902px;left:613px;width:520px">
  <li>A large network of expert consultants who are the best at what they do,</li>
  <li>Service providers all over the world to provide the resources and value that are right for you, available 24 x 7.</li>
</ul>
<p class="abs lead" style="top:2012px;left:613px;width:520px">People are invariably at the center of our customer’s success. Find out how we can add our experts to yours.</p>
<div class="btn" style="top:2092px;left:613px;width:135px;height:44px">Out Team</div>

<!-- testimonials -->
<div class="abs testimonials" role="img" aria-label="Faded photo of business people in an office"></div>
<h2 class="abs" style="top:2338px;left:0;width:1200px;text-align:center;font-size:44px">TESTIMONIALS</h2>
<div class="photo" style="top:2449px;left:525px;width:150px;height:171px;background:linear-gradient(180deg,#d8d8d8,#7a7a7a 70%,#3a3a3a)" role="img" aria-label="Portrait of client Theo Carden"></div>
<div class="photo" style="top:2554px;left:66px;width:76px;height:76px;border-radius:50%;background:linear-gradient(135deg,#c8d0d6,#3a4650)" role="img" aria-label="Client portrait thumbnail"></div>
<div class="photo" style="top:2408px;left:1082px;width:50px;height:50px;border-radius:50%;background:linear-gradient(135deg,#f1e3d6,#c79a72)" role="img" aria-label="Client portrait thumbnail"></div>
<span class="abs" style="top:2478px;left:144px;width:6px;height:6px;border-radius:50%;background:#34e0b0"></span>
<span class="abs" style="top:2536px;left:1043px;width:14px;height:14px;border-radius:50%;background:#f5a623"></span>
<span class="abs" style="top:2668px;left:900px;width:5px;height:5px;border-radius:50%;background:#8a6ee0"></span>
<div class="abs" style="top:2651px;left:0;width:1200px;text-align:center;font-size:20px">Theo Carden</div>
<div class="abs" style="top:2680px;left:0;width:1200px;text-align:center;font-size:13px">August 2019</div>
<div class="abs" style="top:2720px;left:0;width:1200px;text-align:center;font-size:17px;color:#f5a623;letter-spacing:3px">★★★★★</div>
<div class="arrow" style="left:64px"><svg width="96" height="50" viewBox="0 0 96 50"><path d="M66 25H30M42 13L30 25l12 12" stroke="#fff" stroke-width="3" fill="none"/></svg></div>
<div class="arrow" style="left:1040px"><svg width="96" height="50" viewBox="0 0 96 50"><path d="M30 25h36M54 13l12 12-12 12" stroke="#fff" stroke-width="3" fill="none"/></svg></div>
<p class="abs" style="top:2767px;left:190px;width:820px;text-align:center;font-size:15px;line-height:25px">Sed ut perspiciatis unde omnis iste natus error sit voluptatem accusantium doloremque laudantium, totam rem aperiam, eaque ipsa quae ab illo inventore veritatis et quasi architecto beatae vitae dicta sunt explicabo. Nemo enim ipsam voluptatem quia voluptas sit aspernatur aut odit aut fugit.</p>

<svg class="abs" style="top:2880px;left:0" width="1200" height="90" viewBox="0 0 1200 90">
  <path d="M0 0 C250 70 600 90 800 80 C980 70 1110 40 1200 8 L1200 90 L0 90Z" fill="#0a2134"/>
  <path d="M700 80 C900 78 1080 40 1200 0 L1200 14 C1080 60 900 84 700 80Z" fill="#f5c518"/>
</svg>

<!-- technology -->
<h2 class="abs" style="top:2990px;left:0;width:1200px;text-align:center;font-size:44px">TECHNOLOGY</h2>
<div class="tech-card" style="left:66px;background:linear-gradient(160deg,#8fb4cc,#2a4f73 55%,#1b2f45)" role="img" aria-label="Consultant touching a digital data interface"><span>Technology Strategy</span></div>
<div class="tech-card" style="left:429px;background:linear-gradient(160deg,#3f5b72,#21384c 55%,#15212d)" role="img" aria-label="Developers working together at a laptop with code"><span>Leadership &amp; Resourcing</span></div>
<div class="tech-card" style="left:792px;background:linear-gradient(160deg,#5d6c78,#34424e 55%,#1f2a33)" role="img" aria-label="Businessman with a digital globe and customer support graphics"><span>Process Improvements</span></div>

<!-- footer -->
<footer class="abs footer"></footer>
<div class="abs brand" style="top:3622px;left:66px;font-size:54px">Corvanta</div>
<p class="abs" style="top:3717px;left:66px;width:270px;font-size:13px;line-height:21px">We do more for our customers than implement software. We listen. We work to understand...</p>
<span class="abs" style="top:3811px;left:66px;width:40px;height:40px;border-radius:50%;background:var(--blue)"></span>
<span class="abs" style="top:3811px;left:122px;width:40px;height:40px;border-radius:50%;border:2px solid #fff"></span>
<span class="abs" style="top:3811px;left:176px;width:40px;height:40px;border-radius:50%;border:2px solid #fff"></span>

<div class="vline" style="left:376px"></div>
<div class="vline" style="left:676px"></div>
<div class="vline" style="left:873px"></div>

<div class="f-head" style="left:421px">Services</div>
<ul class="f-list" style="left:421px">
  <li>Transformation Planning &amp; Support</li><li>ERP Solutions</li><li>Data &amp; Business Intelligence</li><li>CRM Solutions</li>
</ul>
<div class="f-head" style="left:719px">Quick Links</div>
<ul class="f-list" style="left:719px">
  <li>Home</li><li>About Us</li><li>Services</li><li>Insights</li><li>Join Us</li><li>Contact Us</li>
</ul>
<div class="f-head" style="left:914px">Contact Us</div>
<div class="abs" style="top:3676px;left:914px;width:230px;font-size:13px;line-height:19px;display:flex;gap:8px">
  <svg width="13" height="13" viewBox="0 0 24 24" style="margin-top:3px;flex:none"><path fill="#fff" d="M12 3l10 9h-3v9h-5v-6h-4v6H5v-9H2z"/></svg>
  <span>48 Harlow Street,<br>Brennick 42QT UK</span>
</div>
<div class="abs" style="top:3755px;left:914px;font-size:13px;display:flex;gap:8px;align-items:center">
  <svg width="12" height="12" viewBox="0 0 24 24"><path fill="#fff" d="M6.6 10.8a15.1 15.1 0 0 0 6.6 6.6l2.2-2.2a1 1 0 0 1 1-.25 11.4 11.4 0 0 0 3.6.57 1 1 0 0 1 1 1V20a1 1 0 0 1-1 1A17 17 0 0 1 3 4a1 1 0 0 1 1-1h3.5a1 1 0 0 1 1 1c0 1.25.2 2.45.57 3.6a1 1 0 0 1-.25 1z"/></svg>
  +2 (555) 240 7310
</div>
<div class="abs" style="top:3817px;left:914px;font-size:13px;display:flex;gap:8px;align-items:center">
  <svg width="13" height="11" viewBox="0 0 24 18"><path fill="#fff" d="M0 0h24v18H0zM2 2v1l10 7 10-7V2z"/></svg>
  info@corvanta.com
</div>
<div class="abs" style="top:3947px;left:0;width:1200px;text-align:center;font-size:12px;color:#9fb0bd">© 2023 ALL RIGHTS RESERVED.</div>

</body>
</html>
```